Vital Shield Max is a new Chinese herbal medicine nutritional supplement.

I need a label design for my Dr Pelman Rx Chinese herbal supplement line .
I am launching a new super powerful immune booster
Vital Shield Max.
The FRONT label 3 in. x 4 in. Black mylar bag will have 30 capsules
The Back label will be the size 3 inches x 3 inches will send information
Target Market(s)
Females 25 to 80 who buy nutritional supplements for themselves and their families.
Industry/Entity Type
Medicine
Font styles to use
Decorative
Colors
Designer to choose colors to be used in the design.
Requirements
Must have
- Dr Pelman Rx the name of the company. A wax seal with the an imprint of the name stamp letters on wax .. examples will be provided below.. an image of name stamp inside wax seal. Product name is Vital Shield Max. Must use traditional Chinese colors. COLORS BELOW IN SAVED IMAGES.. GOLD, BLOOD RED, DARK PURPLE. description of product... Powerful Immune Booster.. a clear and easy to read label. ALL SO BACK LABEL 3 INCHES X 3 INCHES USING ONLY TWO COLORS.. BASIC PRODUCT LABEL OF INGREDIENTS, SUGGESTED USE, PRODUCT INFO, AND WARNINGS. IMAGES FILE 3 IS TO BE USED IN WAX SEAL.USE ONLY EXAMPLE COLORS BELOW IN IMAGES
Nice to have
- I like royal colors of ancient China, which happen to be strong psychological colors for marketing. A Gold wax with my name stamp in red or something like that. "Ancient Chinese secret for modern health".
Should not have

```html
<!DOCTYPE html>
<html lang="en">
<head>
<meta charset="utf-8">
<title>Dr Pelman Rx – Vital Shield Max label options</title>
<link rel="stylesheet" href="https://fonts.googleapis.com/css2?family=Alegreya:wght@700&family=Cormorant+Garamond:ital,wght@1,600&family=Archivo+Black&display=swap">
<style>
  :root {
    --canvas: #ffffff;
    --frame: #333333;
    --purple: #472d62;
    --title-white: #f4f1f6;
    --title-lime: #b4d11e;
    --gold-dark: #a98a3e;
    --gold-light: #e6d08c;
    --stripe-red: #e0394a;
    --stripe-blue: #3b3c9a;
    --seal-red: #e0441a;
    --seal-red-deep: #b02a08;
    --seal-red-ink: #9c2406;
    --seal-green: #7aa812;
    --seal-green-deep: #4d7205;
    --seal-green-ink: #c4e53a;
    --badge-light: #9cc75a;
    --badge-deep: #6f9a3a;
    --white: #ffffff;
  }
  html, body {
    margin: 0;
    padding: 0;
    width: 1200px;
    height: 808px;
    overflow: hidden;
    background: var(--canvas);
  }
  .sheet {
    position: relative;
    width: 1198px;
    height: 806px;
    border: 1px solid var(--frame);
  }
  .label {
    position: absolute;
    top: 33px;
    width: 558px;
    height: 744px;
    background: var(--purple);
    overflow: hidden;
    border: 1px solid #2a1a3c;
  }
  .label--red { left: 23px; }
  .label--green { left: 607px; }

  .brand {
    position: absolute;
    top: 86px;
    left: 0;
    width: 100%;
    margin: 0;
    text-align: center;
    font-family: "Alegreya", Georgia, serif;
    font-weight: 700;
    font-size: 64px;
    line-height: 1;
    color: var(--title-white);
  }
  .label--green .brand { color: var(--title-lime); }

  .gold-band {
    position: absolute;
    top: 333px;
    left: 0;
    width: 100%;
    height: 56px;
    background: linear-gradient(90deg, var(--gold-dark), var(--gold-light) 50%, var(--gold-dark));
  }
  .stripes {
    position: absolute;
    top: 420px;
    left: 0;
    width: 100%;
    height: 58px;
    background: repeating-linear-gradient(180deg, var(--stripe-red) 0 3px, transparent 3px 9px);
  }
  .label--green .stripes {
    background: repeating-linear-gradient(180deg, var(--stripe-blue) 0 3px, transparent 3px 9px);
  }

  .seal {
    position: absolute;
    left: 102px;
    top: 190px;
    width: 360px;
    height: 360px;
  }
  .seal svg { display: block; width: 100%; height: 100%; }

  .product-name {
    position: absolute;
    left: 102px;
    top: 262px;
    width: 360px;
    margin: 0;
    text-align: center;
    font-family: "Cormorant Garamond", Georgia, serif;
    font-style: italic;
    font-weight: 600;
    font-size: 66px;
    line-height: 62px;
    color: var(--seal-red-ink);
  }
  .label--green .product-name { color: var(--seal-green-ink); }
  .product-name span { display: block; }
  .product-name .line-1 { margin-left: -40px; }
  .product-name .line-3 { margin-left: 80px; }

  .count {
    position: absolute;
    left: 54px;
    top: 645px;
    width: 110px;
    margin: 0;
    font-family: "Archivo Black", Arial, sans-serif;
    color: var(--white);
    line-height: 1;
    text-align: center;
  }
  .count__number { display: block; font-size: 36px; }
  .count__unit { display: block; font-size: 20px; margin-top: 2px; }

  .badge {
    position: absolute;
    left: 348px;
    top: 540px;
    width: 180px;
    height: 180px;
    border-radius: 50%;
    background: radial-gradient(circle at 45% 40%, var(--badge-light), var(--badge-deep));
  }
  .badge__text {
    position: absolute;
    left: 0;
    top: 62px;
    width: 100%;
    margin: 0;
    text-align: center;
    font-family: "Archivo Black", Arial, sans-serif;
    font-size: 16px;
    line-height: 19px;
    color: var(--white);
  }
</style>
</head>
<body>
<main class="sheet">

  <section class="label label--red" aria-label="Label option in blood red">
    <h1 class="brand">Dr Pelman Rx</h1>
    <div class="gold-band"></div>
    <div class="stripes"></div>
    <div class="seal" role="img" aria-label="Red wax seal pressed with the product name">
      <svg viewBox="0 0 360 360">
        <defs>
          <radialGradient id="wax-red" cx="45%" cy="40%" r="60%">
            <stop offset="0" stop-color="#e0441a"/>
            <stop offset="1" stop-color="#b02a08"/>
          </radialGradient>
        </defs>
        <circle cx="180" cy="180" r="176" fill="#ffffff" opacity="0.35"/>
        <circle cx="180" cy="180" r="168" fill="url(#wax-red)"/>
      </svg>
    </div>
    <h2 class="product-name"><span class="line-1">Vital</span><span class="line-2">Shield</span><span class="line-3">Max</span></h2>
    <p class="count"><span class="count__number">30</span><span class="count__unit">capsules</span></p>
    <div class="badge" role="img" aria-label="Round immune booster emblem">
      <p class="badge__text">Powerful<br>Immune<br>Booster.</p>
    </div>
  </section>

  <section class="label label--green" aria-label="Label option in green">
    <h1 class="brand">Dr Pelman Rx</h1>
    <div class="gold-band"></div>
    <div class="stripes"></div>
    <div class="seal" role="img" aria-label="Green wax seal pressed with the product name">
      <svg viewBox="0 0 360 360">
        <defs>
          <radialGradient id="wax-green" cx="45%" cy="40%" r="60%">
            <stop offset="0" stop-color="#7aa812"/>
            <stop offset="1" stop-color="#4d7205"/>
          </radialGradient>
        </defs>
        <circle cx="180" cy="180" r="176" fill="#ffffff" opacity="0.35"/>
        <circle cx="180" cy="180" r="168" fill="url(#wax-green)"/>
      </svg>
    </div>
    <h2 class="product-name"><span class="line-1">Vital</span><span class="line-2">Shield</span><span class="line-3">Max</span></h2>
    <p class="count"><span class="count__number">30</span><span class="count__unit">capsules</span></p>
    <div class="badge" role="img" aria-label="Round immune booster emblem">
      <p class="badge__text">Powerful<br>Immune<br>Booster.</p>
    </div>
  </section>

</main>
</body>
</html>
```